Book Cover Design Project

I would like a book cover designed for a book entitled: Bright Days Ahead: Finding the Right Tooth Artist
The target audience is those patients interested in cosmetic dentistry. Generally those would be people over 45, with above average income, but the cover should have more universal appeal.
The book was written by
Marcus T. Whitfield, DDS, FSFOC
Fellow in the Society of Family Oral Care
(that's me)
The book will be distributed as an ebook for free to patients and potential patients interested in cosmetic dentistry.

```html
<!DOCTYPE html>
<html lang="en">
<head>
<meta charset="utf-8">
<title>Bright Days Ahead – Book Cover</title>
<link rel="stylesheet" href="https://fonts.googleapis.com/css2?family=Graduate&family=Arimo:wght@400;700&display=swap">
<style>
  :root {
    --page-bg: #c9d0d2;
    --cover-white: #ffffff;
    --title-blue: #4d6791;
    --band-pink: #f7a1b4;
    --subtitle-red: #cc4236;
    --author-sky: #a9d3e9;
    --fine-grey: #5b6b7a;
    --skin-light: #f3d9c9;
    --skin-mid: #e8bba6;
    --lip-pink: #e58d97;
  }
  * { box-sizing: border-box; margin: 0; padding: 0; }
  html, body { width: 1200px; height: 900px; overflow: hidden; }
  body { background: var(--page-bg); position: relative; }

  .book-cover {
    position: absolute; left: 274px; top: 25px;
    width: 651px; height: 850px;
    background: var(--cover-white);
    box-shadow: 0 2px 10px rgba(0,0,0,0.18);
  }
  .photo {
    position: absolute;
    background: linear-gradient(160deg, var(--skin-light), var(--skin-mid));
  }
  .photo--tall   { left: 8px;   top: 10px;  width: 205px; height: 418px; background: linear-gradient(170deg, #f4e2d6, var(--skin-mid) 60%, var(--lip-pink) 80%, #f1d6c6); }
  .photo--lips   { left: 223px; top: 10px;  width: 205px; height: 207px; background: radial-gradient(ellipse at 55% 55%, #fff 0 18%, var(--lip-pink) 30%, var(--skin-light) 70%); }
  .photo--rest   { left: 438px; top: 10px;  width: 205px; height: 207px; background: linear-gradient(160deg, #ffffff, var(--skin-light) 55%, var(--skin-mid)); }
  .photo--mirror { left: 223px; top: 227px; width: 205px; height: 201px; background: radial-gradient(ellipse at 50% 50%, #c96a72 0 25%, var(--lip-pink) 40%, var(--skin-light) 75%); }
  .photo--man    { left: 438px; top: 227px; width: 205px; height: 201px; background: linear-gradient(160deg, #d9b49c, #c99a80 60%, #e9e4e0); }

  .title-top {
    position: absolute; left: 8px; top: 438px; width: 635px; height: 82px;
    font-family: "Graduate", serif; font-size: 76px; line-height: 82px;
    color: var(--title-blue); text-align: center; white-space: nowrap; letter-spacing: -1px;
  }
  .title-band {
    position: absolute; left: 8px; top: 528px; width: 635px; height: 182px;
    background: var(--band-pink); overflow: hidden;
    font-family: "Graduate", serif; font-size: 168px; line-height: 182px;
    color: var(--cover-white); text-align: center; white-space: nowrap;
  }
  .subtitle {
    position: absolute; left: 8px; top: 720px; width: 410px; height: 120px;
    background: var(--subtitle-red); color: var(--cover-white);
    font-family: "Arimo", sans-serif; font-weight: 700; font-size: 36px; line-height: 41px;
    display: flex; align-items: center; justify-content: center; text-align: center;
  }
  .author {
    position: absolute; left: 428px; top: 720px; width: 215px; height: 120px;
    background: var(--author-sky);
    display: flex; flex-direction: column; align-items: center; justify-content: center;
    text-align: center;
  }
  .author__name {
    font-family: "Graduate", serif; color: var(--title-blue);
    font-size: 25px; line-height: 30px; letter-spacing: 1px;
  }
  .author__name span { display: block; }
  .author__name .surname { font-size: 28px; }
  .author__credentials {
    margin-top: 6px; font-family: "Arimo", sans-serif; font-size: 7.5px; color: var(--fine-grey);
  }
</style>
</head>
<body>
  <main class="book-cover">
    <div class="photo photo--tall" role="img" aria-label="Close-up photo of a smiling woman with bright white teeth"></div>
    <div class="photo photo--lips" role="img" aria-label="Close-up photo of a broad smile with white teeth"></div>
    <div class="photo photo--rest" role="img" aria-label="Photo of a young woman smiling, chin resting on her hand"></div>
    <div class="photo photo--mirror" role="img" aria-label="Close-up photo of an open mouth with a dental mirror"></div>
    <div class="photo photo--man" role="img" aria-label="Photo of a smiling middle-aged man"></div>

    <h1 class="title-top">BRIGHT DAYS</h1>
    <div class="title-band">AHEAD</div>

    <h2 class="subtitle">Finding the Right<br>Tooth Artist</h2>

    <div class="author">
      <p class="author__name"><span>MARCUS T.</span><span class="surname">WHITFIELD</span></p>
      <p class="author__credentials">DDS, FSFOC / Fellow in the Society of Family Oral Care</p>
    </div>
  </main>
</body>
</html>
```